Redesign of Plastic Surgeon Website to fully responsive / modern feel

Hi

Our current website is out of date www.harbourlinecosmetic.org

We want a fresh / modern looking design
Needs to be fully responsive design that works extremely well on ipad and mobile device

Would like design for both full screen website and mobile

Have listed a few websites of other plastic surgeons we like
http://www.reformclinicdaily.com/
http://www.peterholtbymd.com/
http://www.corvanbeauty.com/
http://www.tidewellcontouring.com/

Menu needs to include
1. About Us
2. Procedures (see current website for example)
3. News
4. Patient Resources
5. Contact Us

We are flexible with colours / images / layout

I have uploaded a document that has some content - the face pages content is completed only

some of the procedures can have content upwards of 4000 words - total website can be large with over 40,000 words
Updates

Target Market(s)

Mainly women 20-60 85% of practice
Some men 15%

Industry/Entity Type

Plastic Surgery

Number of Pages Required

5+ page

Requirements
Must have
• We need designs for
• Homepage
• Internal pages
• 1. Landing pages for breast / body / face / non surgical main pages
• 2. Procedure pages for individual pages under each section - eg breast augmentation
• 3. About us pages - like meet the doctor, our staff, clinics
• 4. Contact page
• 5. Blog / News page
Nice to have
• See our list of websites for examples of designs we like
• Like full screen design with nice hero image
• Needs to have good to call to action messages on home page like
• Specials, procedure of the month, etc

```html
<!DOCTYPE html>
<html lang="en">
<head>
<meta charset="utf-8">
<title>Patient Stories and Clients</title>
<link rel="stylesheet" href="https://fonts.googleapis.com/css2?family=Cinzel:wght@400;600&family=Lato:wght@400;700&display=swap">
<style>
:root{
  --blue:#1a62ad;
  --blue-dark:#14508f;
  --ink:#1b1b1b;
  --text:#6a6a6a;
  --muted:#8a8a8a;
  --band:#f4f4f4;
  --dark:#222222;
  --dark-line:#474747;
  --footer:#e4e4e4;
  --card-line:#d6d6d6;
}
*{margin:0;padding:0;box-sizing:border-box}
html,body{width:1200px;height:1200px;overflow:hidden;background:#fff}
body{position:relative;font-family:'Lato',sans-serif;color:var(--text)}
.abs{position:absolute}

/* blog cards */
.post-card{position:absolute;top:0;width:278px;height:169px;border:1px solid var(--card-line);border-top:none;background:#fff;padding:12px 13px 0 13px}
.post-meta{font-size:10.5px;color:var(--muted);display:flex;align-items:center;gap:4px;height:16px}
.post-meta svg{flex:none}
.post-meta .gap{width:8px}
.post-excerpt{margin-top:12px;font-size:11.5px;line-height:18.2px;color:var(--muted)}
.read-more{display:inline-block;margin-top:11px;background:var(--blue);color:#fff;font-size:10.5px;font-weight:700;padding:6px 14px;border-radius:12px;letter-spacing:-.1px}

/* testimonials */
.testimonials{position:absolute;left:0;top:213px;width:1200px;height:446px;background:var(--band);text-align:center}
.quote-mark{position:absolute;left:580px;top:42px}
.section-title{font-family:'Cinzel',serif;font-weight:400;color:var(--ink);font-size:29px;letter-spacing:.5px}
.testimonials .section-title{position:absolute;left:0;width:1200px;top:89px}
.tagline{position:absolute;left:0;width:1200px;top:132px;font-size:10.5px;color:var(--ink)}
.testimony{position:absolute;left:195px;width:810px;top:178px;font-size:18px;line-height:26.5px;color:var(--text)}
.avatar{position:absolute;left:566px;top:263px;width:68px;height:68px;border-radius:50%;background:radial-gradient(circle at 50% 45%,#c9a58a 0 30%,#6d5b45 55%,#3f5a2e 100%)}
.author{position:absolute;left:0;width:1200px;top:344px;font-size:11.5px;font-weight:700;color:var(--ink)}
.author span{color:var(--blue);font-weight:700}
.slider-dots{position:absolute;left:580px;top:395px}

/* clients */
.clients .section-title{position:absolute;left:0;width:1200px;top:692px;text-align:center}
.clients-intro{position:absolute;left:220px;width:760px;top:734px;text-align:center;font-size:12px;line-height:19px;color:var(--text)}
.client-tile{position:absolute;top:818px;width:139px;height:64px;border:1px dashed #d4d4d4;display:flex;align-items:center;justify-content:center;gap:6px;font-size:11px;font-weight:700;color:var(--blue-dark);text-align:center;line-height:13px}
.client-tile i{display:block;width:10px;height:10px;border-radius:50%;background:var(--blue-dark);flex:none}

/* call to action */
.cta-band{position:absolute;left:0;top:927px;width:1200px;height:163px;background:var(--dark)}
.cta-box{position:absolute;left:95px;top:38px;width:997px;height:116px;border:2px solid var(--dark-line)}
.cta-icon{position:absolute;left:61px;top:29px}
.cta-lead{position:absolute;left:108px;top:25px;color:#fff;font-size:22px;font-weight:700;letter-spacing:-.2px}
.cta-main{position:absolute;left:108px;top:56px;color:#fff;font-size:23.5px;font-weight:700;letter-spacing:-.1px}
.cta-button{position:absolute;left:763px;top:36px;width:188px;height:43px;border-radius:22px;background:var(--blue);color:#fff;font-size:16.5px;display:flex;align-items:center;justify-content:center}
.cta-edge{position:absolute;left:0;top:1089px}
.footer-band{position:absolute;left:0;top:1096px;width:1200px;height:104px;background:var(--footer)}
</style>
</head>
<body>

<!-- blog cards -->
<article class="post-card" style="left:162px">
  <div class="post-meta">
    <svg width="10" height="10" viewBox="0 0 10 10"><circle cx="5" cy="3" r="2.4" fill="#999"/><path d="M0.5 10c0-3 2-4.5 4.5-4.5S9.5 7 9.5 10z" fill="#999"/></svg>
    Posted By: ram<span class="gap"></span>
    <svg width="11" height="10" viewBox="0 0 11 10"><ellipse cx="5.5" cy="4.5" rx="5.3" ry="4" fill="#999"/><path d="M2 7l-1 3 3-2z" fill="#999"/></svg> 1
  </div>
  <p class="post-excerpt">Lorem Ipsum is simply dummy text of the printing and typesetting industry. Lorem Ipsum has been the industry's standard dummy text ever since the 1500s, when an .....</p>
  <span class="read-more">READ MORE</span>
</article>
<article class="post-card" style="left:461px">
  <div class="post-meta">
    <svg width="10" height="10" viewBox="0 0 10 10"><circle cx="5" cy="3" r="2.4" fill="#999"/><path d="M0.5 10c0-3 2-4.5 4.5-4.5S9.5 7 9.5 10z" fill="#999"/></svg>
    Posted By: ram<span class="gap"></span>
    <svg width="11" height="10" viewBox="0 0 11 10"><ellipse cx="5.5" cy="4.5" rx="5.3" ry="4" fill="#999"/><path d="M2 7l-1 3 3-2z" fill="#999"/></svg> 1
  </div>
  <p class="post-excerpt">Lorem Ipsum is simply dummy text of the printing and typesetting industry. Lorem Ipsum has been the industry's standard dummy text ever since the 1500s, when an .....</p>
  <span class="read-more">READ MORE</span>
</article>
<article class="post-card" style="left:760px">
  <div class="post-meta">
    <svg width="10" height="10" viewBox="0 0 10 10"><circle cx="5" cy="3" r="2.4" fill="#999"/><path d="M0.5 10c0-3 2-4.5 4.5-4.5S9.5 7 9.5 10z" fill="#999"/></svg>
    Posted By: ram<span class="gap"></span>
    <svg width="11" height="10" viewBox="0 0 11 10"><ellipse cx="5.5" cy="4.5" rx="5.3" ry="4" fill="#999"/><path d="M2 7l-1 3 3-2z" fill="#999"/></svg> 1
  </div>
  <p class="post-excerpt">Lorem Ipsum is simply dummy text of the printing and typesetting industry. Lorem Ipsum has been the industry's standard dummy text ever since the 1500s, when an .....</p>
  <span class="read-more">READ MORE</span>
</article>

<!-- testimonials -->
<section class="testimonials">
  <svg class="quote-mark" width="40" height="32" viewBox="0 0 40 32">
    <path d="M16 4C8 6 2 12 2 20a8 8 0 1 0 8-8c0-3 3-6 7-6z" fill="var(--blue)"/>
    <path d="M37 4C29 6 23 12 23 20a8 8 0 1 0 8-8c0-3 3-6 7-6z" fill="var(--blue)"/>
  </svg>
  <h2 class="section-title">WHAT OUR PATIENT HAVE TO SAY</h2>
  <p class="tagline">WE ARE RELIABLE AND TRUSTED</p>
  <p class="testimony">Lorem Ipsum is simply dummy text of the printing and typesetting industry. Lorem Ipsum has been the in-dustry's standard dummy text ever since the 1500s, when an .....unknown printer took..</p>
  <div class="avatar" role="img" aria-label="Portrait photo of the patient giving the testimonial"></div>
  <p class="author">DANIEL MORROW, <span>BRIGHTFIELD STUDIO</span></p>
  <svg class="slider-dots" width="54" height="14" viewBox="0 0 54 14">
    <circle cx="6" cy="7" r="4.2" fill="var(--blue)"/>
    <circle cx="19" cy="7" r="5.3" fill="none" stroke="var(--blue)" stroke-width="2"/>
    <circle cx="33" cy="7" r="4.2" fill="var(--blue)"/>
    <circle cx="47" cy="7" r="4.2" fill="var(--blue)"/>
  </svg>
</section>

<!-- clients -->
<section class="clients">
  <h2 class="section-title">OUR CLIENTS</h2>
  <p class="clients-intro">Lorem Ipsum is simply dummy text of the printing and typesetting industry.Ipsum has been the industry's standrd ....dummy text ever since the 150when an unknown printer took a galley otype and scrambled it to make a type specimen book. It has survived not on</p>
  <div class="client-tile" style="left:153px"><i></i>Meridian Guild</div>
  <div class="client-tile" style="left:303px"><i></i>Coastline Society</div>
  <div class="client-tile" style="left:454px"><i></i>Northfield Society</div>
  <div class="client-tile" style="left:604px"><i></i>Aesthetic Circle</div>
  <div class="client-tile" style="left:759px"><i></i>Lumen Union</div>
  <div class="client-tile" style="left:910px"><i></i>Valecrest Medical</div>
</section>

<!-- call to action -->
<section class="cta-band">
  <div class="cta-box">
    <svg class="cta-icon" width="26" height="26" viewBox="0 0 26 26">
      <path d="M13 5H3v18h18V13" fill="none" stroke="#fff" stroke-width="2.6"/>
      <path d="M21 2l4 4-11 11-5 1 1-5z" fill="#fff"/>
    </svg>
    <p class="cta-lead">Need a Doctor For Check - Up?</p>
    <p class="cta-main">JUST MAKE AN APOINTMENT &amp; YOU’RE DONE!</p>
    <span class="cta-button">Get An Appointment</span>
  </div>
</section>
<svg class="cta-edge" width="1200" height="8" viewBox="0 0 1200 8">
  <defs>
    <pattern id="teeth" width="11" height="8" patternUnits="userSpaceOnUse">
      <polygon points="0,0 11,0 5.5,7" fill="var(--dark)"/>
    </pattern>
  </defs>
  <rect width="1200" height="8" fill="var(--footer)"/>
  <rect width="1200" height="8" fill="url(#teeth)"/>
</svg>
<div class="footer-band"></div>

</body>
</html>
```